Need 4 childhood cancer facts posters

Hello. I run a nonprofit in East Tennessee, USA that supports children with cancer and their families.

I need 4 poster designs with facts about childhood cancers. It should either have pictures of children with cancer or be focused around the whole idea of childhood cancer awareness. This project will require time and research. I will post links to facts as the project goes forward.

Questions can be emailed to tmerrow@glowwithnora.org. AI format of our logo has been uploaded. I have images and links here http://www.glowwithnora.org/contest-pics.html

You can also view our website at www.glowwithnora.org

Some facts: http://pelt.tumorstats.example/archive/publications/childhood/

USE THESE FACTS: * Everyday, approximately 250 children will die from childhood cancer. *Childhood Cancers is the number 1 cause of death in children under age 15 in the US. *Less than 5% of the federal governments budget toward cancer research is dedicated to childhood cancers. *One in 330 children will be diagnosed with cancer by the time they are 20.

Poster will be 24 inches wide by 36 inches tall.

```html
<!DOCTYPE html>
<html lang="en">
<head>
<meta charset="utf-8">
<title>Childhood Cancer Awareness Poster</title>
<link rel="stylesheet" href="https://fonts.googleapis.com/css2?family=Arvo:wght@400;700&display=swap">
<style>
  :root {
    --sky-light: #bdb6aa;
    --sky-mid: #8f877b;
    --sky-dark: #4f4940;
    --ink: #141210;
    --rope: #8a6a45;
    --pin: #c9a477;
    --frame: #f6f4ef;
    --photo-a: #8fb3c9;
    --photo-b: #d3a98c;
    --logo-gold: #e2c13c;
    --logo-ink: #1f1c18;
    --portrait-top: #cdb7a6;
    --portrait-bottom: #d9d8d3;
  }
  * { box-sizing: border-box; margin: 0; padding: 0; }
  html, body { width: 800px; height: 1200px; overflow: hidden; }
  body { font-family: "Arvo", Georgia, serif; color: var(--ink); }

  .poster {
    position: relative;
    width: 800px;
    height: 1200px;
    overflow: hidden;
    background:
      radial-gradient(ellipse 520px 420px at 50% 45%, rgba(230,224,212,0.75), rgba(230,224,212,0) 70%),
      linear-gradient(180deg, var(--sky-mid) 0%, var(--sky-light) 35%, var(--sky-mid) 70%, var(--sky-dark) 100%);
  }

  .headline {
    position: absolute;
    top: 74px;
    left: 0;
    width: 800px;
    text-align: center;
    font-weight: 700;
    font-size: 25px;
    line-height: 32px;
  }

  .clothesline { position: absolute; top: 0; left: 0; width: 800px; height: 420px; }

  .snapshot {
    position: absolute;
    background: var(--frame);
    padding: 8px 8px 24px;
    box-shadow: 2px 4px 8px rgba(0,0,0,0.35);
  }
  .snapshot .photo {
    width: 100%;
    height: 100%;
    background: linear-gradient(160deg, var(--photo-a), var(--photo-b));
  }
  .snap-1 { left: 12px;  top: 248px; width: 120px; height: 128px; transform: rotate(-14deg); }
  .snap-2 { left: 180px; top: 252px; width: 128px; height: 134px; transform: rotate(8deg); }
  .snap-3 { left: 342px; top: 246px; width: 126px; height: 140px; transform: rotate(-3deg); }
  .snap-4 { left: 502px; top: 244px; width: 132px; height: 130px; transform: rotate(5deg); }
  .snap-5 { left: 660px; top: 236px; width: 126px; height: 140px; transform: rotate(-2deg); }

  .facts {
    position: absolute;
    top: 404px;
    left: 0;
    width: 800px;
    text-align: center;
    font-weight: 700;
    font-size: 17px;
    line-height: 32px;
  }
  .facts p { margin-bottom: 37px; }

  .foundation {
    position: absolute;
    left: 50px;
    top: 704px;
    display: flex;
    align-items: center;
    gap: 10px;
  }
  .foundation .dot {
    width: 22px; height: 22px;
    border-radius: 50%;
    background: var(--logo-gold);
  }
  .foundation .name {
    font-weight: 400;
    font-size: 14px;
    line-height: 1.25;
    color: var(--logo-ink);
    width: 160px;
  }

  .child-portrait {
    position: absolute;
    left: 258px;
    top: 706px;
    width: 370px;
    height: 494px;
    background: linear-gradient(180deg, var(--portrait-top), var(--portrait-bottom));
  }
</style>
</head>
<body>
<main class="poster">
  <h1 class="headline">Everyday, approximately 250 children<br>will die from childhood cancer.</h1>

  <svg class="clothesline" viewBox="0 0 800 420" aria-hidden="true">
    <path d="M0 246 Q400 252 800 228" fill="none" stroke="var(--rope)" stroke-width="4"/>
    <rect x="52"  y="226" width="9" height="36" rx="2" fill="var(--pin)"/>
    <rect x="224" y="232" width="9" height="36" rx="2" fill="var(--pin)"/>
    <rect x="382" y="232" width="9" height="36" rx="2" fill="var(--pin)"/>
    <rect x="548" y="228" width="9" height="36" rx="2" fill="var(--pin)"/>
    <rect x="718" y="218" width="9" height="36" rx="2" fill="var(--pin)"/>
  </svg>

  <figure class="snapshot snap-1"><div class="photo" role="img" aria-label="Snapshot of a child smiling with family"></div></figure>
  <figure class="snapshot snap-2"><div class="photo" role="img" aria-label="Snapshot of children together outdoors"></div></figure>
  <figure class="snapshot snap-3"><div class="photo" role="img" aria-label="Snapshot of a child holding a stuffed toy"></div></figure>
  <figure class="snapshot snap-4"><div class="photo" role="img" aria-label="Snapshot of a child with a parent"></div></figure>
  <figure class="snapshot snap-5"><div class="photo" role="img" aria-label="Snapshot of a child playing outside"></div></figure>

  <section class="facts">
    <p>Childhood Cancers is the number 1 cause of death<br>in children under age 15 in the US.</p>
    <p>Less than 5% of the federal governments budget<br>toward cancer research is dedicated to childhood cancers.</p>
    <p>One in 330 children will be diagnosed with cancer<br>by the time they are 20.</p>
  </section>

  <div class="foundation">
    <span class="dot"></span>
    <span class="name">Nora Merrow Childhood Cancer Foundation</span>
  </div>

  <div class="child-portrait" role="img" aria-label="Photo of a bald child wearing a white face mask, looking up"></div>
</main>
</body>
</html>
```